Business cards for property management company

Need new business cards designed for our property management company and rental community, Amber Knoll Commons. These cards will be primarily picked up by rental applicants.

May be single or double sided design.

I need cards for two different people, listed below. The design can be the same for both, and the only information that will be different is name and email address.

Industry/Entity Type

Property Management

Requirements
Must have
• US standard business card - 2''x3.5'' horizontal design.

1. Logo (attached). The text does not have to stay below the logo, but the card does need to say "Amber Knoll Commons" somewhere on it (does not have to be same font as logo, but those fonts are Americana Extra Bold and BlackJack if needed).
2. Name: one with "Lena Halvorsen" and one with "Dorian Halvorsen"
3. Email address: one with "lena@amberknollhub.com" and one with "dorian@amberknollhub.com"
4. Web address: amberknollhub.com
5. Phone: 281.555.0182
6. Address: 7390 Whitlock Avenue, Cedarport, Oregon 77512 (zip code may me omitted, at your discretion)
Should not have
• No rounded corners or special cuts.

No bevel, emboss or shadow effects.

As a note, please do not use our website as a basis for color or design schemes. We are working on a redesign, based around the new logo (attached to brief).

```html
<!DOCTYPE html>
<html lang="en">
<head>
<meta charset="utf-8">
<title>Amber Knoll Commons – Business Cards</title>
<link rel="stylesheet" href="https://fonts.googleapis.com/css2?family=Josefin+Sans:wght@400;600&family=Poiret+One&display=swap">
<style>
  :root {
    --page-bg: #ece9e4;
    --card-lime: #cdd26a;
    --card-glow: #fbf35a;
    --card-ice: #d9fdfd;
    --band-blue: #1697c9;
    --name-green: #3c9a2c;
    --brand-green: #2f8f3a;
    --contact-yellow: #f3e34c;
    --contact-blue: #1b8fc4;
    --white: #ffffff;
  }
  * { margin: 0; padding: 0; box-sizing: border-box; }
  html, body { width: 1200px; height: 900px; overflow: hidden; }
  body {
    background: var(--page-bg);
    position: relative;
    font-family: "Josefin Sans", sans-serif;
  }
  .card { position: absolute; width: 650px; height: 370px; overflow: hidden; }

  /* Front card */
  .card--lena {
    left: 136px; top: 81px;
    background: radial-gradient(circle at 46% 40%, var(--card-glow) 0, #e6e064 18%, var(--card-lime) 40%);
  }
  .card--lena .holder-name {
    position: absolute; left: 24px; top: 28px;
    color: var(--name-green); font-size: 17px; letter-spacing: 0.5px; text-transform: uppercase;
  }
  .brand-name {
    position: absolute; color: var(--brand-green); font-weight: 600; text-align: center; line-height: 1.1;
  }
  .card--lena .brand-name { left: 215px; top: 128px; width: 170px; font-size: 19px; }
  .card--lena .contact-band {
    position: absolute; left: 0; top: 272px; width: 650px; height: 98px;
    background: var(--band-blue); border-top-right-radius: 16px;
    color: var(--contact-yellow); font-size: 15px;
  }
  .contact-band .address { position: absolute; left: 24px; top: 12px; line-height: 38px; }
  .contact-band .address span { display: block; }
  .contact-band .address span + span { padding-left: 3px; }
  .contact-band .online { position: absolute; left: 356px; top: 10px; line-height: 28px; }
  .contact-band .online span { display: block; }
  .contact-band .online .phone { padding-left: 52px; }

  /* Second card */
  .card--dorian { left: 468px; top: 482px; background: var(--card-ice); }
  .name-tab {
    position: absolute; left: 216px; top: 0; width: 216px; height: 58px;
    background: var(--band-blue); border-radius: 0 0 12px 12px;
    color: var(--white); font-family: "Poiret One", sans-serif; font-size: 22px;
    display: flex; align-items: center; justify-content: center; text-transform: uppercase;
  }
  .card--dorian .contact-list {
    position: absolute; left: 31px; top: 218px;
    color: var(--contact-blue); font-size: 15px; line-height: 26px;
  }
  .card--dorian .contact-list span { display: block; }
  .card--dorian .brand-name { left: 500px; top: 282px; width: 140px; font-size: 16px; }
  .base-strip { position: absolute; left: 0; top: 341px; }
</style>
</head>
<body>
  <section class="card card--lena">
    <p class="holder-name">Lena Halvorsen</p>
    <p class="brand-name">Amber Knoll Commons</p>
    <div class="contact-band">
      <p class="address"><span>Address: 7390 Whitlock Avenue,</span><span>Cedarport, Oregon 77512</span></p>
      <p class="online">
        <span>Email address: lena@amberknollhub.com</span>
        <span>Web address: amberknollhub.com</span>
        <span class="phone">Phone: 281.555.0182</span>
      </p>
    </div>
  </section>

  <section class="card card--dorian">
    <p class="name-tab">Dorian Halvorsen</p>
    <p class="contact-list">
      <span>Address: 7390 Whitlock Avenue,</span>
      <span>Cedarport, Oregon 77512</span>
      <span>Web address: amberknollhub.com</span>
      <span>Email address: dorian@amberknollhub.com</span>
      <span>Phone: 281.555.0182</span>
    </p>
    <p class="brand-name">Amber Knoll Commons</p>
    <svg class="base-strip" width="650" height="29" viewBox="0 0 650 29" aria-hidden="true">
      <path d="M0 0 H220 Q216 14 230 14 H420 Q434 14 430 0 H650 V29 H0 Z" fill="var(--band-blue)"/>
    </svg>
  </section>
</body>
</html>
```